Kestrin Supply Website Redesign

Currently kestrinsupply.example is focussed on fulfillment and transport from various products in the BBQ segment. However, no we want to update our business activities to Product Development, Brand Development, Online Positioning, Logistics & Aftersales, and Promotional BBQs. We will be a business for Outdoor Leisure Development from A to Z.

Therefore, we need a brand new website. The colours of the current website may be the same. However, i'd like to keep it clean. More white and use blue and green as accent colours. It is a business to business organization so the website should be looking formal and corporate. However we sell fun products so not too formal and corporate.

Pages we need; Home, About, Contact, Our Services (+ page per service) a place to share our news/blogs.

I have added some sort of mock up of an idea. However it needs some finetuning.

Businesses

Corporate/Logistics/Marketing

Coded - Design and coding required

Designer to choose colors to be used in the design.

• Show clear distinguishing of the different services we provide (Product Development, Brand Development, Online Positioning, Logistics & Aftersales and Promotional BBQs). Every service should have its own page too. Besides, I would like to have a blog page to share relevant content.
• Show that we are the expert in Outdoor LEisure Development from A to Z
• Be too informal. It may be semi-formal

```html
<!DOCTYPE html>
<html lang="en">
<head>
<meta charset="utf-8">
<title>Kestrin Supply – Outdoor Leisure Development</title>
<link href="https://fonts.googleapis.com/css2?family=Poppins:wght@400;500;600;700&display=swap" rel="stylesheet">
<style>
:root{
  --teal:#3d6571;
  --teal-dark:#2f5460;
  --green:#3fa535;
  --navy:#1c1a4f;
  --ink:#1f2a44;
  --text:#444;
  --muted:#777;
  --light:#f5f6f6;
  --white:#fff;
}
*{margin:0;padding:0;box-sizing:border-box}
html,body{width:1200px;height:3452px;overflow:hidden}
body{font-family:'Poppins',sans-serif;color:var(--text);background:var(--white);position:relative}
.abs{position:absolute}
a{color:inherit;text-decoration:none}

/* top bar */
.topbar{left:0;top:0;width:1200px;height:51px;background:var(--teal);color:#fff;font-size:14px}
.topbar .green{right:0;top:0;height:51px;width:345px;background:var(--green);clip-path:polygon(30px 0,100% 0,100% 100%,0 100%)}
.topbar span{position:absolute;top:16px}
.flag{display:inline-block;width:20px;height:13px;background:linear-gradient(#c8102e 50%,#fff 50%);background-size:100% 4px;vertical-align:-2px;margin-right:6px;position:relative}
.flag::after{content:"";position:absolute;left:0;top:0;width:9px;height:7px;background:#3c3b6e}
.dot-icon{display:inline-block;width:12px;height:12px;border-radius:50%;background:#fff;margin-left:16px;vertical-align:-1px}

/* nav */
.nav{left:0;top:51px;width:1200px;height:103px;background:#fff}
.brand{display:flex;align-items:center;gap:12px;font-weight:700;color:var(--teal);font-size:48px;letter-spacing:1px}
.brand i{display:block;width:34px;height:34px;border-radius:50%;background:var(--green)}
.menu{right:110px;top:46px;display:flex;gap:41px;font-size:16px;color:#333}

/* hero */
.hero{left:0;top:154px;width:1200px;height:724px}
.hero-photo{left:0;top:0;width:1200px;height:724px;background:linear-gradient(100deg,#3a2c22 0%,#6f5440 40%,#b08a66 65%,#8a6a52 100%);clip-path:polygon(0 0,100% 0,100% 92%,0 100%)}
.hero-band{left:0;top:666px;width:849px;height:58px;background:var(--green);clip-path:polygon(0 38%,100% 0,100% 16%,0 100%)}
.hero h1{left:110px;top:170px;font-size:56px;line-height:64px;color:#fff;font-weight:700}
.hero h1 span{font-weight:400}
.hero p{left:110px;top:314px;width:470px;font-size:14.5px;line-height:30px;color:#fff}
.btn{display:inline-flex;align-items:center;justify-content:center;gap:10px;border-radius:10px;color:#fff;font-weight:600;font-size:16px}
.hero .btn{left:110px;top:463px;width:181px;height:50px;background:var(--teal)}
.counter{left:30px;color:#fff;font-size:15px}
.vline{left:37px;top:240px;width:2px;height:252px;background:rgba(255,255,255,.6)}
.vline::before{content:"";position:absolute;left:0;top:20px;width:2px;height:70px;background:var(--green)}
.dots{left:515px;top:628px;display:flex;gap:8px}
.dots i{display:block;width:30px;height:4px;background:#fff;border-radius:2px}
.dots i:first-child{width:56px;background:var(--green)}

/* section titles */
.title{font-weight:700;color:var(--ink);font-size:42px;text-align:center;width:1200px;left:0}
.title-mark{width:80px;height:80px;border-radius:50%;border:1px dashed rgba(63,165,53,.35);background:repeating-linear-gradient(135deg,rgba(63,165,53,.12) 0 2px,transparent 2px 5px)}

/* services */
.card{top:1053px;width:207px;height:256px;background:#fff;border-radius:8px;box-shadow:0 2px 10px rgba(0,0,0,.14);text-align:center;padding-top:36px}
.card svg{width:80px;height:80px}
.card h3{color:var(--green);font-size:18px;line-height:23px;font-weight:600;margin-top:16px}
.card p{font-size:12.5px;line-height:18px;color:#333;margin-top:12px;padding:0 18px}

/* cases */
.cases{left:0;top:1412px;width:1200px;height:754px;background:var(--teal);clip-path:polygon(0 0,100% 58px,100% 100%,0 94%)}
.cases-band-top{left:600px;top:1428px;width:600px;height:50px;background:var(--green);clip-path:polygon(0 0,100% 38px,100% 50px,0 14px)}
.cases-band-bot{left:0;top:2128px;width:489px;height:36px;background:var(--green);clip-path:polygon(0 0,100% 20px,100% 100%,0 60%)}
.case{top:1602px;width:301px;height:454px;background:#fff;clip-path:polygon(0 0,100% 0,100% 91%,0 100%);text-align:center}
.case .ph{height:241px}
.case .badge{position:absolute;left:116px;top:206px;width:70px;height:70px;border-radius:50%;background:var(--green);display:flex;align-items:center;justify-content:center}
.case h4{margin-top:52px;font-size:16px;font-weight:600;color:#222}
.case p{margin-top:14px;font-size:13px;line-height:27px;color:var(--muted);padding:0 18px}
.arrow{top:1809px;width:48px;height:48px;border-radius:50%;border:2px solid #fff;display:flex;align-items:center;justify-content:center}

/* about */
.about-photo{left:70px;top:2297px;width:474px;height:346px;border-radius:18px;background:linear-gradient(110deg,#e27a2c 0%,#b9c3d0 35%,#7a95b8 65%,#3b5f9a 100%)}
.about h2{left:606px;top:2300px;font-size:38px;line-height:46px;color:var(--ink);font-weight:600}
.about p{left:607px;top:2410px;width:480px;font-size:15px;line-height:32px;color:#333}
.about .btn{left:607px;top:2584px;width:143px;height:46px;background:var(--green);border-radius:23px}

/* partners */
.partners{left:0;top:2756px;width:1200px;height:420px;background:var(--light)}
.partner{top:2950px;height:100px;display:flex;align-items:center;justify-content:center;font-weight:600;font-size:30px;color:var(--ink)}
.partner.dark{background:#1b1a18;color:#fff;font-size:20px}

/* footer */
.footer{left:0;top:3104px;width:1200px;height:348px;background:var(--navy);clip-path:ellipse(90% 100% at 50% 100%)}
.footer-box{left:0;top:3140px;width:1200px;height:312px;background:var(--navy)}
.footer .col,.fcol{color:#fff;font-size:15px;line-height:35px}
.fcol h5{color:var(--green);font-size:19px;font-weight:600;margin-bottom:0}
.social{display:flex;gap:18px;margin-top:8px}
.social i{display:block;width:20px;height:20px;border-radius:50%;background:#fff}
</style>
</head>
<body>

<!-- top bar -->
<div class="abs topbar">
  <div class="abs green"></div>
  <span style="left:110px"><i class="flag"></i>English ⌄</span>
  <span style="left:425px">☎ Phone: +31 (0)10 555 0148</span>
  <span style="left:641px">✉ info@kestrinsupply.example</span>
  <span style="left:905px">Login/Signup</span>
  <span style="left:1028px"><i class="dot-icon"></i><i class="dot-icon"></i></span>
</div>

<!-- nav -->
<header class="abs nav">
  <div class="abs brand" style="left:110px;top:26px"><i></i>Kestrin</div>
  <nav class="abs menu"><a>Home</a><a>About</a><a>Our Services</a><a>Blog</a><a>Contact</a></nav>
</header>

<!-- hero -->
<section class="abs hero">
  <div class="abs hero-photo" role="img" aria-label="Woman shopping online with a laptop and payment card in a warm kitchen"></div>
  <div class="abs hero-band"></div>
  <div class="abs counter" style="top:205px">01</div>
  <div class="abs vline"></div>
  <div class="abs counter" style="top:472px">04</div>
  <h1 class="abs">E-Commerce &amp;<br><span>Order Portals</span></h1>
  <p class="abs">We believe that the partners we work for should be able to focus on building their brand and product. Kestrin Supply therefore takes care of the process from order processing to delivery. Together with our Partner Kestrin Promotional,</p>
  <a class="abs btn">Get Started
    <svg width="14" height="14" viewBox="0 0 14 14"><circle cx="7" cy="7" r="7" fill="#fff"/><path d="M6 4l3 3-3 3" stroke="#3d6571" stroke-width="2" fill="none"/></svg></a>
  <div class="abs dots"><i></i><i></i><i></i><i></i></div>
</section>

<!-- services -->
<div class="abs title-mark" style="left:470px;top:924px"></div>
<h2 class="abs title" style="top:938px;left:30px">Our Services</h2>

<div class="abs card" style="left:55px">
  <svg viewBox="0 0 80 80" fill="none" stroke="#1a1a1a" stroke-width="2.5"><circle cx="40" cy="40" r="30" stroke="#3fa535" stroke-width="8" stroke-dasharray="8 5"/><circle cx="40" cy="40" r="22"/><path d="M30 34l10-6 10 6v12l-10 6-10-6z M30 34l10 6 10-6 M40 40v12"/></svg>
  <h3>PRODUCT<br>DEVELOPMENT</h3><p>Increase turnover through automated order processes</p>
</div>
<div class="abs card" style="left:277px">
  <svg viewBox="0 0 80 80" fill="none" stroke="#1a1a1a" stroke-width="2.5"><circle cx="40" cy="34" r="24"/><path d="M40 22l4 8 9 1-7 6 2 9-8-5-8 5 2-9-7-6 9-1z" fill="#3fa535"/><path d="M22 50l-8 16 10-2 4 9 8-14 M58 50l8 16-10-2-4 9-8-14"/></svg>
  <h3>BRAND<br>DEVELOPMENT</h3><p>Assembly &amp; Fine-grained distribution on a project basis</p>
</div>
<div class="abs card" style="left:499px">
  <svg viewBox="0 0 80 80" fill="none" stroke="#1a1a1a" stroke-width="2.5"><rect x="12" y="16" width="56" height="38" rx="2"/><path d="M6 60h68v4H6z"/><circle cx="34" cy="34" r="5" stroke="#3fa535"/><path d="M25 50c2-6 16-6 18 0"/><rect x="46" y="22" width="16" height="10" rx="2" stroke="#3fa535"/></svg>
  <h3>ONLINE<br>POSITIONING</h3><p>Storage, Order Processing &amp; Shipping</p>
</div>
<div class="abs card" style="left:721px">
  <svg viewBox="0 0 80 80" fill="none" stroke="#1a1a1a" stroke-width="2.5"><path d="M8 22h40v34H8z M48 34h14l10 10v12H48z"/><circle cx="20" cy="60" r="5" fill="#fff"/><circle cx="60" cy="60" r="5" fill="#fff"/><path d="M4 16h20" stroke="#3fa535"/></svg>
  <h3>LOGISTICS &amp;<br>AFTERSALES</h3><p>Setting up &amp; managing Loyalty programs</p>
</div>
<div class="abs card" style="left:939px">
  <svg viewBox="0 0 80 80" fill="none" stroke="#1a1a1a" stroke-width="2.5"><path d="M14 46l36-28 8 30-38 4z"/><path d="M20 52l6 14h6l-4-14" stroke="#3fa535"/><path d="M62 20l6-4 M64 30h8 M60 12l2-6" stroke="#3fa535"/></svg>
  <h3>PROMOTIONAL<br>BBQS</h3><p>Setting up &amp; managing Loyalty programs</p>
</div>

<!-- cases -->
<div class="abs cases"></div>
<div class="abs cases-band-top"></div>
<div class="abs cases-band-bot"></div>
<div class="abs title-mark" style="left:478px;top:1480px;opacity:.5"></div>
<h2 class="abs title" style="top:1494px;left:14px;color:#fff">Our Cases</h2>

<div class="abs arrow" style="left:43px"><svg width="16" height="16" viewBox="0 0 16 16"><path d="M10 2L4 8l6 6" stroke="#fff" stroke-width="2" fill="none"/></svg></div>
<div class="abs arrow" style="left:1109px"><svg width="16" height="16" viewBox="0 0 16 16"><path d="M6 2l6 6-6 6" stroke="#fff" stroke-width="2" fill="none"/></svg></div>

<div class="abs case" style="left:111px">
  <div class="ph" role="img" aria-label="Team reviewing plans in a warehouse office" style="background:linear-gradient(160deg,#c9d3dc,#5c6f86)"></div>
  <div class="badge"><svg width="36" height="36" viewBox="0 0 36 36" fill="none" stroke="#fff" stroke-width="2"><circle cx="18" cy="18" r="14" stroke-dasharray="5 3"/><path d="M12 15l6-4 6 4v7l-6 4-6-4z"/></svg></div>
  <h4>Lorem ipsum dolor</h4><p>Lorem ipsum dolor sit amet, consectetur adipiscing elit, sed do eiusmod tempor incididunt ut labore et</p>
</div>
<div class="abs case" style="left:451px">
  <div class="ph" role="img" aria-label="Hands working with a tablet and keyboard at a desk" style="background:linear-gradient(160deg,#eef1f4,#9aa7b5)"></div>
  <div class="badge"><svg width="36" height="36" viewBox="0 0 36 36" fill="none" stroke="#fff" stroke-width="2"><circle cx="18" cy="12" r="5"/><path d="M6 26c4-6 8-6 12-2 4-4 8-4 12 2"/></svg></div>
  <h4>Lorem ipsum dolor</h4><p>Lorem ipsum dolor sit amet, consectetur adipiscing elit, sed do eiusmod tempor incididunt ut labore et</p>
</div>
<div class="abs case" style="left:789px">
  <div class="ph" role="img" aria-label="Man paying online with a card at a laptop" style="background:linear-gradient(160deg,#6b6560,#2f3b52)"></div>
  <div class="badge"><svg width="36" height="36" viewBox="0 0 36 36" fill="none" stroke="#fff" stroke-width="2"><circle cx="18" cy="20" r="10"/><path d="M12 8a8 8 0 0112 0 M9 5a12 12 0 0118 0"/></svg></div>
  <h4>Lorem ipsum dolor</h4><p>Lorem ipsum dolor sit amet, consectetur adipiscing elit, sed do eiusmod tempor incididunt ut labore et</p>
</div>

<!-- about -->
<div class="abs about-photo" role="img" aria-label="Forklift moving through a warehouse with tall shelving"></div>
<div class="abs title-mark" style="left:580px;top:2294px"></div>
<section class="about">
  <h2 class="abs">Kestrin Supply ensures<br>silent distribution</h2>
  <p class="abs">Ensures the smooth distribution of promotional merchandise products for its customers. With our own warehouse and fleet, we are able to get products to the right place quickly and reliably, from small orders to larger, complex deliveries to multiple addresses.</p>
  <a class="abs btn">Read More</a>
</section>

<!-- partners -->
<div class="abs partners"></div>
<div class="abs title-mark" style="left:455px;top:2798px"></div>
<h2 class="abs title" style="top:2812px;left:14px">Our Partners</h2>
<div class="abs partner" style="left:100px;width:190px;gap:10px"><i style="display:block;width:28px;height:28px;border-radius:50%;background:#d9374b"></i>Kestrin</div>
<div class="abs partner" style="left:340px;width:180px;font-weight:400;color:#8a8a8a">Saucery</div>
<div class="abs partner" style="left:545px;width:190px;font-size:26px">Emberline</div>
<div class="abs partner dark" style="left:769px;width:124px;height:124px;top:2928px">Coalbox</div>
<div class="abs partner" style="left:925px;width:180px;font-size:24px">Smokestack</div>

<!-- footer -->
<div class="abs footer"></div>
<div class="abs footer-box"></div>
<div class="abs brand" style="left:115px;top:3242px;color:#fff;font-size:46px"><i style="background:#d7d7de"></i>Kestrin</div>
<div class="abs fcol" style="left:115px;top:3318px;font-size:13.5px;line-height:23px">2021 Copyright © Kestrin Supply<br>All Right Reserved</div>
<div class="abs fcol" style="left:417px;top:3210px">
  <h5>Site Map</h5>Home<br>About Us<br>Our Services<br>Contact Us
</div>
<div class="abs fcol" style="left:629px;top:3210px;line-height:27px">
  <h5 style="margin-bottom:6px">Contact Info</h5>Lindenlaan 12,<br>3011 AB Rotterdam<br><span style="display:block;margin-top:8px">+31 (0)10 555 0148</span><span style="display:block;margin-top:8px">info@kestrinsupply.example</span>
</div>
<div class="abs fcol" style="left:878px;top:3210px">
  <h5>Follow Us</h5>
  <div class="social"><i></i><i></i><i></i><i></i><i></i></div>
</div>

</body>
</html>
```